Brantley Advisory Group provides support for renewable energy projects to utilities and suppliers

I need a professional looking business card that is both simple and elegant and unique. My clients are mostly large organizations not individuals. I am a consultant with my own company that is small but would like to give clients the impression I am larger. Smart grid, fiber optics, software, field hardware, distribution automation, substation automation, operations, energy storage/batteries, microgrids, customer service, strategy/roadmaps, conservation, Automated Metering Infrastruture (AMI or smart meters) are all areas of focus.

Target Market(s)

Utilities, suppliers, governmental agencies involved in energy. All types of energy especially natural gas and electrical. Especially renewable energy or green projects.

Contact Information for Business Card

Name - Mark Brantley Cell Phone - 425.318.2746 Email - mbrantley@brantleyag-example.com
Company - Brantley Advisory Group (logo) Title - Principal

Font styles to use
Serif
Sans Serif

Colors

Designer to choose colors to be used in the design.

Requirements
Must have
• Simple and professional and powerful.
• Unique/creative design.
Nice to have
• Utilize color scheme to accent logo colors. Maybe some geometric pattern on edge of card with color.
Should not have
• Busy, complicated, traditional

```html
<!DOCTYPE html>
<html lang="en">
<head>
<meta charset="utf-8">
<title>Brantley Advisory Group – Business Card</title>
<link href="https://fonts.googleapis.com/css2?family=Montserrat:wght@600;800&family=Raleway:wght@400;500&display=swap" rel="stylesheet">
<style>
  :root {
    --bg: #e4e4ec;
    --card: #f7f7f5;
    --blue: #2a2fa8;
    --blue-soft: #a9abd9;
    --green: #6f9a3e;
    --green-soft: #c9d6b6;
    --grey-soft: #d6d6d8;
  }
  * { margin: 0; padding: 0; box-sizing: border-box; }
  html, body { width: 1200px; height: 858px; overflow: hidden; background: var(--bg); }
  .stage { position: relative; width: 1200px; height: 858px; }
  .card {
    position: absolute; top: 280px; width: 520px; height: 297px;
    background: var(--card); overflow: hidden;
    box-shadow: 0 6px 18px rgba(60, 60, 90, 0.18);
  }
  .card--front { left: 50px; }
  .card--back { left: 630px; }
  .bands { position: absolute; inset: 0; }
  .brand {
    position: absolute; display: flex; align-items: center; gap: 10px;
    font-family: "Montserrat", sans-serif; font-weight: 600; color: var(--blue);
  }
  .card--front .brand { top: 30px; right: 34px; font-size: 17px; }
  .card--back .brand { top: 34px; right: 38px; font-size: 18px; }
  .brand__mark { width: 16px; height: 16px; background: var(--green); }
  .person { position: absolute; top: 118px; right: 62px; text-align: right; }
  .person__name {
    font-family: "Montserrat", sans-serif; font-weight: 800; font-size: 26px;
    letter-spacing: 2px; color: var(--blue); text-transform: uppercase;
  }
  .person__title {
    font-family: "Raleway", sans-serif; font-weight: 400; font-size: 19px;
    letter-spacing: 1px; color: var(--green); margin-top: 2px;
  }
  .contact {
    position: absolute; top: 200px; right: 62px; text-align: right;
    font-family: "Raleway", sans-serif; font-weight: 500; font-size: 11.5px;
    line-height: 22px; color: var(--green); letter-spacing: 0.5px;
  }
  .contact-tab {
    position: absolute; top: 194px; right: 0; width: 40px; height: 74px;
    background: var(--blue); border-radius: 6px 0 0 6px;
    display: flex; flex-direction: column; align-items: center; justify-content: space-around;
    padding: 6px 0;
  }
  .contact-tab svg { width: 13px; height: 13px; fill: #fff; }
</style>
</head>
<body>
<div class="stage">

  <section class="card card--front">
    <svg class="bands" viewBox="0 0 520 297" aria-hidden="true">
      <rect x="40" y="0" width="14" height="297" fill="var(--grey-soft)"/>
      <rect x="0" y="150" width="260" height="14" fill="var(--grey-soft)"/>
      <rect x="88" y="0" width="14" height="297" fill="var(--blue-soft)"/>
      <rect x="0" y="90" width="140" height="14" fill="var(--blue-soft)"/>
      <rect x="130" y="0" width="16" height="297" fill="var(--green-soft)"/>
      <rect x="0" y="230" width="200" height="16" fill="var(--green-soft)"/>
    </svg>

    <div class="brand"><span class="brand__mark"></span>Brantley Advisory Group</div>

    <div class="person">
      <h1 class="person__name">Mark Brantley</h1>
      <p class="person__title">Principal</p>
    </div>

    <address class="contact">
      425.318.2746<br>
      mbrantley@brantleyag-example.com<br>
      www.brantleyag-example.com
    </address>

    <div class="contact-tab">
      <svg viewBox="0 0 24 24" aria-label="Phone"><path d="M6.6 10.8a15 15 0 0 0 6.6 6.6l2.2-2.2c.3-.3.7-.4 1-.2 1.1.4 2.3.6 3.6.6.6 0 1 .4 1 1V20c0 .6-.4 1-1 1A17 17 0 0 1 3 4c0-.6.4-1 1-1h3.5c.6 0 1 .4 1 1 0 1.3.2 2.5.6 3.6.1.3 0 .7-.2 1z"/></svg>
      <svg viewBox="0 0 24 24" aria-label="Email"><path d="M2 5h20v14H2z M4 7v.5l8 5 8-5V7l-8 5z" fill-rule="evenodd"/></svg>
      <svg viewBox="0 0 24 24" aria-label="Website"><path d="M5 2l14 11h-7l4 8-3 1.5-4-8L5 19z"/></svg>
    </div>
  </section>

  <section class="card card--back">
    <svg class="bands" viewBox="0 0 520 297" aria-hidden="true">
      <rect x="0" y="150" width="520" height="16" fill="var(--grey-soft)"/>
      <rect x="0" y="100" width="300" height="16" fill="var(--blue-soft)"/>
      <rect x="280" y="100" width="16" height="197" fill="var(--blue-soft)"/>
      <rect x="150" y="190" width="370" height="18" fill="var(--green-soft)"/>
      <rect x="150" y="190" width="18" height="107" fill="var(--green-soft)"/>
    </svg>
    <div class="brand"><span class="brand__mark"></span>Brantley Advisory Group</div>
  </section>

</div>
</body>
</html>
```